Wordpress Design Project - Coded

Our current website is housed with Hostavel
See : www.karnovel.com

We wish to have the functionality of http://old.dimrota.com

I like how the boxes look on the website and having the ability to write notes along with images so it look like a magazine. I want to be able to have the flexibility to include categories for different topics.

Please find my logo attached so you can include it on the website. Also consider this color palette to create the website. The actual logo in PNG will be attached later on.
Updates

I now need to commit to a final design sooner than later.

Target Market(s)

Target market are Breeders from the Equestrian sector.

Requirements
Must have
• 1. The new template must contain everything presently contained in the current website (i.e. www.karnovel.com ) In particular, the membership form and the CoinBrisk payment feature, Ability to expand payment possibilities for Merchandise etc. It should also allow to include video content.

2. The template must allow our font ( TRAJAN PRO ) and color scheme ( see Below ).

3. Logo must be preeminent and " Northern Valor Stud Guild " affixed on the homepage in Trajan Pro font style;

3. We are happy with the look and feel of our simple website. What is lacking is the " Category " feature and our ability to post articles and news features. We wish to see at least six (6) latest articles.

4. I need to keep the new template offline until I am able to migrate all existing data over.

5. Our logo needs to be integrated.

6. Home page should have a button connecting to our Chatterly;

7. Viewer should have the ability to "forward" an article;

8. The name of the association (i.e. The Northern Valor Stud Guild " should appear on the homepage above the logo as it does at www.karnovel.com presently. The copy should in Trajan Pro font.

Nice to have
• 1. Ability to translate articles and content into Spanish
Should not have
• Should NOT have any reference or materials from www.dimrota.com

```html
<!DOCTYPE html>
<html lang="en">
<head>
<meta charset="utf-8">
<title>Northern Valor Stud Guild</title>
<link href="https://fonts.googleapis.com/css2?family=Cinzel:wght@600;700&family=PT+Sans:wght@400;700&family=PT+Sans+Narrow:wght@700&family=Noto+Serif:wght@700&family=Open+Sans:wght@400;600&display=swap" rel="stylesheet">
<style>
:root{
  --red:#d40d12;
  --red-dark:#a8090d;
  --red-deep:#8f0a0c;
  --ink:#2b2b2b;
  --muted:#7a7a7a;
  --line:#dcdcdc;
  --paper:#ffffff;
  --chat-blue:#2f5fa8;
}
*{margin:0;padding:0;box-sizing:border-box}
html,body{width:759px;height:1200px;overflow:hidden;background:var(--paper)}
body{position:relative;font-family:"Open Sans",sans-serif;color:var(--ink)}
.abs{position:absolute}
.top-rule{left:0;top:0;width:759px;height:3px;background:var(--red)}
.brand-mark{left:338px;top:14px;width:82px;height:82px;border-radius:50%;background:radial-gradient(circle at 40% 35%,#e8272b,var(--red-deep))}
.brand-initials{left:300px;top:104px;width:159px;text-align:center;font-family:"Cinzel",serif;font-weight:700;font-size:18px;color:var(--red-dark);letter-spacing:2px}
.guild-name{left:180px;top:140px;width:400px;text-align:center;font-family:"Cinzel",serif;font-weight:700;font-size:15.5px;color:var(--red-dark);letter-spacing:.6px}
.social{top:110px;width:18px;height:18px;border-radius:3px}
.search{left:569px;top:137px;width:141px;height:19px;border:1px solid #cfcfcf;border-radius:10px;font-size:7px;color:#888;padding:4px 9px}
.search svg{position:absolute;right:7px;top:4px}
.nav{left:46px;top:168px;width:668px;height:35px;background:linear-gradient(#e6161b,#c70a0f);display:flex;border-radius:2px 2px 0 0}
.nav a{font-family:"PT Sans Narrow",sans-serif;font-weight:700;font-size:12.5px;color:#fff;text-decoration:none;display:flex;align-items:center;justify-content:center;border-right:1px solid rgba(255,255,255,.35)}
.nav a:last-child{border-right:0}
.hero{left:46px;top:203px;width:668px;height:243px;background:linear-gradient(180deg,#b9cfe9 0%,#8aac6a 30%,#5f8c3a 60%,#9bbb4e 100%)}
.hero-caption{left:46px;top:334px;width:270px;height:80px}
.hero-caption h2{position:absolute;left:15px;top:13px;font-family:"Noto Serif",serif;font-size:13.5px;color:var(--red-dark)}
.hero-caption p{position:absolute;left:17px;top:34px;width:220px;font-size:8.5px;line-height:14px;color:var(--red-dark)}
.dots{left:364px;top:432px;display:flex;gap:2px}
.dots span{width:7px;height:7px;border-radius:50%;border:1px solid #333;background:#fff}
.dots span:first-child{background:#222}
.card{width:215px;height:134px;border:1px solid var(--line);border-radius:2px;background:#fff}
.card h3{position:absolute;left:16px;top:9px;font-family:"PT Sans",sans-serif;font-weight:400;font-size:13px;line-height:16.5px;color:var(--red)}
.card .thumb{position:absolute;left:14px;top:49px;width:72px;height:64px}
.card p{position:absolute;left:94px;top:49px;width:115px;font-size:7.2px;line-height:13px;color:var(--muted)}
.card .more{position:absolute;left:95px;top:104px;font-size:7.5px;color:var(--ink)}
.cats{left:514px;top:460px;width:198px;height:347px;border:1px solid var(--line)}
.cats h3{height:33px;background:linear-gradient(#e6161b,#c70a0f);color:#fff;font-family:"PT Sans",sans-serif;font-weight:400;font-size:14px;padding:7px 16px}
.cats ul{list-style:none;padding:10px 0 0 20px}
.cats li{font-size:7.5px;height:18.2px;color:var(--ink);position:relative;padding-left:12px}
.cats li::before{content:"";position:absolute;left:0;top:2px;border-left:4px solid #aaa;border-top:3.5px solid transparent;border-bottom:3.5px solid transparent}
.video{left:514px;top:814px;width:198px;height:144px;border:1px solid var(--line);padding:5px 7px}
.video .screen{width:100%;height:100%;background:linear-gradient(160deg,#5a5a4a,#2a2a24);border:3px solid #111}
.join{left:514px;top:964px;width:198px;height:100px;border:1px solid var(--line);background:linear-gradient(#fff,#f1f1f1)}
.join h3{position:absolute;left:16px;top:10px;font-family:"PT Sans",sans-serif;font-weight:400;font-size:14px;color:var(--ink)}
.join p{position:absolute;left:16px;top:33px;font-size:7.5px;color:var(--muted)}
.join .btn{position:absolute;left:18px;top:53px;width:124px;height:25px;border-radius:3px;background:linear-gradient(#4a78c0,var(--chat-blue));color:#fff;font-weight:600;font-size:8px;padding:7px 9px}
.join .btn i{position:absolute;right:0;top:0;width:26px;height:25px;border-left:1px solid rgba(255,255,255,.4)}
.news-head{left:52px;top:904px;font-family:"PT Sans",sans-serif;font-size:14px;color:var(--ink)}
.news{width:215px}
.news h4{font-family:"PT Sans",sans-serif;font-weight:700;font-size:10px;color:var(--ink);margin-bottom:4px}
.news p{font-size:7.2px;line-height:13px;color:var(--muted)}
.footer{left:0;top:1112px;width:759px;height:88px;background:linear-gradient(var(--red),var(--red-deep))}
.footer nav{position:absolute;left:53px;top:24px;font-family:"PT Sans",sans-serif;font-weight:700;font-size:9.5px;color:#fff}
.footer small{position:absolute;left:53px;top:47px;font-size:6.5px;color:#fff}
</style>
</head>
<body>
<div class="abs top-rule"></div>

<header>
  <div class="abs brand-mark"></div>
  <div class="abs brand-initials">NVSG</div>
  <h1 class="abs guild-name">Northern Valor Stud Guild</h1>
  <span class="abs social" style="left:638px;background:#1f6fb0"></span>
  <span class="abs social" style="left:661px;background:#3b5d9e"></span>
  <span class="abs social" style="left:684px;background:#3b8ee0"></span>
  <div class="abs search">Search here..
    <svg width="10" height="10" viewBox="0 0 10 10"><circle cx="4" cy="4" r="3" fill="none" stroke="#999" stroke-width="1.3"/><line x1="6.3" y1="6.3" x2="9.3" y2="9.3" stroke="#999" stroke-width="1.5"/></svg>
  </div>
</header>

<nav class="abs nav">
  <a style="width:67px">Home</a>
  <a style="width:81px">About Us</a>
  <a style="width:129px">Mission Statement</a>
  <a style="width:125px">Membership Form</a>
  <a style="width:90px">Stud Book</a>
  <a style="width:99px">Horses For Sale</a>
  <a style="width:77px">Press</a>
</nav>

<section class="abs hero" role="img" aria-label="Black horse galloping across a green meadow with trees"></section>
<div class="abs hero-caption">
  <svg width="270" height="80" viewBox="0 0 270 80" style="position:absolute;left:0;top:0"><polygon points="0,0 245,0 270,40 245,80 0,80" fill="rgba(255,255,255,.88)"/></svg>
  <h2>The First PRE Breeders Association</h2>
  <p>Phasellus felis dolor, scelerisque a, tempus eget, lobortis . Donec scelerisque leo ac risus.</p>
</div>
<div class="abs dots"><span></span><span></span><span></span><span></span></div>

<main>
  <article class="abs card" style="left:51px;top:460px"><h3>Duis tincidunt<br>lectus dui viverra</h3><div class="thumb" role="img" aria-label="Mare and foal grazing" style="background:linear-gradient(#6f9a3e,#8b5a2b)"></div><p>Nunc tempus felis vitae urna. Vivamus porttitor, g, purus nisi eleifend libero, a tempus libero lectus feugiat felis.</p><span class="more">Learn More</span></article>
  <article class="abs card" style="left:275px;top:460px"><h3>Proin nulla<br>arcu nonummy luctus</h3><div class="thumb" role="img" aria-label="Bay horse head close-up" style="background:linear-gradient(90deg,#5d8a3c,#8a4e2a)"></div><p>Nunc tempus felis vitae urna. Vivamus porttitor, g, purus nisi eleifend libero, a tempus libero lectus feugiat felis.</p><span class="more">Learn More</span></article>
  <article class="abs card" style="left:51px;top:605px"><h3>Curabitur metus<br>ipsum luctus eu</h3><div class="thumb" role="img" aria-label="Rider seated on a carousel horse" style="background:linear-gradient(#d9d2c2,#a07a55)"></div><p>Nunc tempus felis vitae urna. Vivamus porttitor, g, purus nisi eleifend libero, a tempus libero lectus feugiat felis.</p><span class="more">Learn More</span></article>
  <article class="abs card" style="left:275px;top:605px"><h3>Maecenas aliquet<br>velit vel turpis</h3><div class="thumb" role="img" aria-label="Girl hugging a brown horse" style="background:linear-gradient(90deg,#e05a8a,#5a3420)"></div><p>Nunc tempus felis vitae urna. Vivamus porttitor, g, purus nisi eleifend libero, a tempus libero lectus feugiat felis.</p><span class="more">Learn More</span></article>
  <article class="abs card" style="left:51px;top:749px"><h3>Phasellus felis<br>scelerisque tempus</h3><div class="thumb" role="img" aria-label="Chestnut horse in a stable yard" style="background:linear-gradient(90deg,#6b3a1c,#c9b89a)"></div><p>Nunc tempus felis vitae urna. Vivamus porttitor, g, purus nisi eleifend libero, a tempus libero lectus feugiat felis.</p><span class="more">Learn More</span></article>
  <article class="abs card" style="left:275px;top:749px"><h3>Etiam est nunc<br>venenatis in tristique eu</h3><div class="thumb" role="img" aria-label="Horses jumping a steeplechase fence" style="background:linear-gradient(#3d78c4,#6d8a4a)"></div><p>Nunc tempus felis vitae urna. Vivamus porttitor, g, purus nisi eleifend libero, a tempus libero lectus feugiat felis.</p><span class="more">Learn More</span></article>

  <h2 class="abs news-head">RECENT NEWS &amp; EVENTS</h2>
  <div class="abs news" style="left:52px;top:932px"><h4>Phasellus felis dolor</h4><p>Etiam nulla massa, pharetra facilisis, volutpat in, imperdiet sit amet, sem. Aliquam nec erat at purus cursus interdum. Vestibulum ligula augue, bibendum accumsan</p></div>
  <div class="abs news" style="left:278px;top:932px"><h4>Maecenas aliquet velit vel turpis</h4><p>Etiam nulla massa, pharetra facilisis, volutpat in, imperdiet sit amet, sem. Aliquam nec erat at purus cursus interdum. Vestibulum ligula augue, bibendum accumsan</p></div>
  <div class="abs news" style="left:52px;top:1007px"><h4>Donec iaculis diam</h4><p>Etiam nulla massa, pharetra facilisis, volutpat in, imperdiet sit amet, sem. Aliquam nec erat at purus cursus interdum. Vestibulum ligula augue, bibendum accumsan</p></div>
  <div class="abs news" style="left:278px;top:1007px"><h4>Class aptent taciti</h4><p>Etiam nulla massa, pharetra facilisis, volutpat in, imperdiet sit amet, sem. Aliquam nec erat at purus cursus interdum. Vestibulum ligula augue, bibendum accumsan</p></div>
</main>

<aside>
  <div class="abs cats">
    <h3>Our Categories</h3>
    <ul>
      <li>VECRA Bulletins</li><li>VECRA Sanctioned Shows Competitions</li><li>International Competitions</li><li>LG-VECRA SERVICE FORMS</li><li>PRE Breed Characteristics</li><li>PRE Breeders</li><li>PRE Breeder’s Corner</li><li>PRE Horse Glossary</li><li>PRE Horses – Featured</li><li>PRE Horses Trainers</li><li>PRE Horses- Art</li><li>PRE Performance Hall of Fame</li><li>PRE Photography</li><li>PRE Recognition Awards</li><li>PRE Resources</li><li>PRE Riders</li>
    </ul>
  </div>
  <div class="abs video">
    <div class="screen" role="img" aria-label="Video still of a horseman in a vehicle">
      <svg width="178" height="126" viewBox="0 0 178 126"><rect x="66" y="46" width="46" height="34" rx="6" fill="rgba(230,230,230,.85)"/><polygon points="83,54 83,72 98,63" fill="#555"/></svg>
    </div>
  </div>
  <div class="abs join">
    <h3>Join Us Chatterly Now</h3>
    <p>Please click here to join with us on Chatterly.</p>
    <div class="btn">Join us on Chatterly<i></i></div>
  </div>
</aside>

<footer class="abs footer">
  <nav>Home&nbsp; / &nbsp;About Us&nbsp; / &nbsp;Mission Statement&nbsp; / &nbsp;Membership Form&nbsp; / &nbsp;Stud Book&nbsp; / &nbsp;Horses For Sale&nbsp; / &nbsp;Press</nav>
  <small>© 2012 Company Name.&nbsp; All right reserved.&nbsp; Term of Use</small>
</footer>
</body>
</html>
```